Brio 41 specialty coffee shop business card

Please use Design #5812047 from previous project (logo design). Brio 41 is a new coffee shop that will serve specialty coffee and will focus on high quality products. I would like to use orange and brown colors. I like designs that are simple but elegant and that deliver a message that is easy to recognize. I will upload a file of the logo design.

Industry/Entity Type

Coffee Shop

Contact Information for Business Card

Leon Cordravik
(555) 203-7719

Font styles to use
Serif
Sans Serif
Script

Requirements
Must have
• simple and elegant, colors match nicely, I like to use orange and brown. Background creme color.
Should not have
• complex designs that are hard to understand.

```html
<!DOCTYPE html>
<html lang="en">
<head>
<meta charset="utf-8">
<title>Brio 41 — Business Cards</title>
<link rel="stylesheet" href="https://fonts.googleapis.com/css2?family=Open+Sans:wght@300;400;600&display=swap">
<style>
  :root {
    --stage: #e8e5e1;
    --card: #fbfbfa;
    --card-edge: #5a5a5a;
    --espresso: #3a1c10;
    --caramel: #c08a45;
    --caramel-soft: rgba(192, 138, 69, 0.28);
    --espresso-soft: rgba(58, 28, 16, 0.22);
  }
  * { box-sizing: border-box; margin: 0; padding: 0; }
  html, body {
    width: 1200px;
    height: 900px;
    overflow: hidden;
  }
  body {
    position: relative;
    background: var(--stage);
    font-family: "Open Sans", Arial, sans-serif;
  }
  .card {
    position: absolute;
    background: var(--card);
    overflow: hidden;
  }
  .card--portrait {
    left: 61px; top: 138px;
    width: 407px; height: 629px;
    border: 1px solid var(--card-edge);
  }
  .card--landscape {
    left: 508px; top: 251px;
    width: 632px; height: 408px;
  }
  .brand {
    position: absolute;
    display: flex;
    align-items: center;
    gap: 12px;
  }
  .brand__dot {
    width: 22px; height: 22px;
    border-radius: 50%;
    background: var(--caramel);
  }
  .brand__name {
    font-weight: 600;
    font-size: 40px;
    color: var(--espresso);
    letter-spacing: 0.5px;
    white-space: nowrap;
  }
  .card--portrait .brand { left: 120px; top: 106px; }
  .card--landscape .brand { left: 418px; top: 116px; }

  .bean-trail {
    position: absolute;
    left: 0; top: 0;
  }
  .contact {
    position: absolute;
    list-style: none;
    color: var(--caramel);
    font-weight: 400;
    font-size: 20px;
    line-height: 31.5px;
    letter-spacing: 0.3px;
  }
  .card--portrait .contact { left: 119px; top: 438px; }
  .card--landscape .contact { left: 52px; top: 245px; }
</style>
</head>
<body>

  <section class="card card--portrait" aria-label="Business card, portrait">
    <svg class="bean-trail" width="407" height="629" viewBox="0 0 407 629" role="img" aria-label="Diagonal trail of scattered brown and tan coffee beans">
      <defs>
        <linearGradient id="trail-portrait" x1="0" y1="0" x2="1" y2="1">
          <stop offset="0" stop-color="var(--espresso-soft)"/>
          <stop offset="1" stop-color="var(--caramel-soft)"/>
        </linearGradient>
      </defs>
      <path d="M15 235 L125 230 L185 285 L230 360 L300 370 L390 410 L390 455 L300 430 L220 385 L160 330 L90 300 L15 260 Z" fill="url(#trail-portrait)"/>
    </svg>
    <div class="brand">
      <span class="brand__dot" aria-hidden="true"></span>
      <span class="brand__name">Brio 41</span>
    </div>
    <ul class="contact">
      <li class="contact__name">Leon Cordravik</li>
      <li class="contact__phone">(555) 203-7719</li>
      <li class="contact__email">hello@brio41.com</li>
    </ul>
  </section>

  <section class="card card--landscape" aria-label="Business card, landscape">
    <svg class="bean-trail" width="632" height="408" viewBox="0 0 632 408" role="img" aria-label="Diagonal trail of scattered brown and tan coffee beans">
      <defs>
        <linearGradient id="trail-landscape" x1="0" y1="0" x2="1" y2="1">
          <stop offset="0" stop-color="var(--caramel-soft)"/>
          <stop offset="1" stop-color="var(--espresso-soft)"/>
        </linearGradient>
      </defs>
      <path d="M20 125 L130 140 L230 175 L300 230 L360 300 L440 315 L615 325 L615 350 L440 355 L350 320 L285 265 L210 215 L120 185 L20 150 Z" fill="url(#trail-landscape)"/>
    </svg>
    <div class="brand">
      <span class="brand__dot" aria-hidden="true"></span>
      <span class="brand__name">Brio 41</span>
    </div>
    <ul class="contact">
      <li class="contact__name">Leon Cordravik</li>
      <li class="contact__phone">(555) 203-7719</li>
      <li class="contact__email">hello@brio41.com</li>
    </ul>
  </section>

</body>
</html>
```